K & K Fabrications Brochure

We need a 2 page (front and back) full color brochure for our Mechanical Contracting company. The website is http://www.kkfabrications.example although we're looking for something fresh. If anything the future web design might follow the design of this brochure more than we'd like to have the brochure follow the design of the website. However, to start please use content found on the website and we will refine. We want basically a cover, 2 inner pages and a back. Attached is a an example brochure from another company as well as an outdated brochure we used previously.

Target Market(s)

1. Industrial, Commercial and Institutional Builders and Owners

2. Industrial, Commercial and Institutional HVAC Service customers

Industry/Entity Type

It Company

Font styles to use
Serif
Sans Serif

Requirements
Must have
• Strong imagery
Should not have
• Plumbing Service
Pictures of people besides Owner Oren Walczak and President Tomas Lindqvist

```html
<!DOCTYPE html>
<html lang="en">
<head>
<meta charset="utf-8">
<title>K &amp; K Fabrications – HVAC &amp; Mechanical Systems</title>
<link href="https://fonts.googleapis.com/css2?family=Lilita+One&family=Open+Sans:wght@700&display=swap" rel="stylesheet">
<style>
  :root {
    --brand-blue: #1b7fe3;
    --brand-blue-text: #2a8cf0;
    --overlay-blue: rgba(24, 122, 230, 0.86);
    --ink: #0b0b0c;
    --white: #ffffff;
    --photo-light: #dfe3e6;
    --photo-mid: #7d8790;
    --photo-dark: #1d1f21;
  }
  * { margin: 0; padding: 0; box-sizing: border-box; }
  html, body { width: 849px; height: 1200px; overflow: hidden; background: var(--white); }
  .brochure-cover {
    position: relative;
    width: 849px;
    height: 1200px;
    overflow: hidden;
    font-family: "Open Sans", Arial, sans-serif;
    background: var(--white);
  }
  .cover-photo {
    position: absolute;
    left: 0; top: 150px;
    width: 849px; height: 1050px;
    background: linear-gradient(180deg, var(--photo-light) 0%, #cfd6dc 28%, #b9c3cb 52%, var(--photo-mid) 70%, #3a3c3e 84%, var(--photo-dark) 100%);
  }
  .cover-graphics {
    position: absolute;
    left: 0; top: 0;
    width: 849px; height: 1200px;
  }
  .brand-mark {
    position: absolute;
    left: 56px; top: 44px;
    display: flex;
    flex-direction: column;
    align-items: flex-start;
    gap: 12px;
  }
  .brand-mark__square {
    width: 88px; height: 88px;
    background: var(--brand-blue);
  }
  .brand-mark__name {
    font-family: "Open Sans", Arial, sans-serif;
    font-weight: 700;
    font-size: 13px;
    line-height: 1;
    color: var(--ink);
    text-transform: uppercase;
    white-space: nowrap;
  }
  .cover-headline {
    position: absolute;
    left: 47px; top: 512px;
    font-family: "Lilita One", "Arial Black", sans-serif;
    font-weight: 400;
    font-size: 50px;
    line-height: 52px;
    letter-spacing: 4.5px;
    color: var(--white);
    text-transform: uppercase;
    white-space: nowrap;
  }
  .cover-contact {
    position: absolute;
    left: 0; top: 1015px;
    width: 849px;
    text-align: center;
    font-style: normal;
    font-weight: 700;
    color: var(--white);
    font-size: 17px;
    line-height: 28px;
  }
  .cover-contact__company {
    color: var(--brand-blue-text);
    font-size: 19px;
  }
  .cover-contact__label { color: var(--brand-blue-text); }
  .cover-contact__sep { margin: 0 14px; }
</style>
</head>
<body>
<main class="brochure-cover">
  <div class="cover-photo" role="img" aria-label="Photograph of crew guiding a large HVAC unit lifted by a hoist inside an open building, winter shoreline beyond"></div>

  <svg class="cover-graphics" viewBox="0 0 849 1200" aria-hidden="true">
    <g class="speed-stripes">
      <polygon fill="#0b0b0c" points="70,238 849,70 849,88 60,258"/>
      <polygon fill="#ffffff" points="0,262 849,88 849,106 0,286"/>
      <polygon fill="#0b0b0c" points="0,286 849,106 849,120 0,300"/>
      <polygon fill="#ffffff" points="0,300 849,120 849,138 0,323"/>
      <polygon fill="#0b0b0c" points="0,323 849,138 849,150 0,338"/>
      <polygon fill="#ffffff" points="0,338 849,150 849,166 0,358"/>
      <polygon fill="#1a1a1a" points="0,358 849,166 849,178 0,372"/>
    </g>
    <polygon class="blue-wedge" fill="rgba(24,122,230,0.86)" points="0,205 849,640 0,1068"/>
  </svg>

  <div class="brand-mark">
    <span class="brand-mark__square"></span>
    <span class="brand-mark__name">K &amp; K Fabrications, Inc</span>
  </div>

  <h1 class="cover-headline">
    Heating,<br>
    Ventilation<br>
    Air Conditioning(HVAC)<br>
    Mechanical Systems
  </h1>

  <address class="cover-contact">
    <div class="cover-contact__company">K &amp; K Fabrications, Inc.</div>
    <div>4470 Larkfield Road Brookvale, WI 53999</div>
    <div><span class="cover-contact__label">Phone:</span> 608-555-0142<span class="cover-contact__sep">::</span><span class="cover-contact__label">Fax:</span> 608-555-0187</div>
  </address>
</main>
</body>
</html>
```